Infographic for a Life Transformation brand to showcase their principle method

I need a clean infographic which would be used in a brochure to show the 5 steps to achieving a Inner Uprising. (ie Life transformation). I use the theme of a revolution so I would like the graphic to include a raised fist or something to represent a revolution and then the 5 points of information to represent each step.
Needs to very clean and simple. I don't want something that would take up a full page, I want it as a graphic, almost like a big logo. I don't want it laid out like a process chart.

My brand personalities from https://markcharacterhub.com.au/ are
The Everyman and The Magician to give you an idea of my brand.

I've attached my logo so that you can see the colour of it. Graphic doesn't need to match logo but should align with that colour.

Target Market(s)

Top Tier Executives, males, 35-55y old

Industry/Entity Type

Life Coaching

Requirements
Must have
• The graphic must have the 5 Steps: in this order
1.Clarity
2. Measurement
3. Discipline
4. Nutrition
5.Exercise
Nice to have
• It could include these action steps which line up with the 5 steps, It may be too much information by there is the option to include if it works.
1.see it
2. track it
3. do it
4. eat it
5. move it

```html
<!DOCTYPE html>
<html lang="en">
<head>
<meta charset="utf-8">
<title>Inner Uprising – Five Steps</title>
<link rel="stylesheet" href="https://fonts.googleapis.com/css2?family=Oswald:wght@400;500&family=Poppins:wght@500&display=swap">
<style>
  :root {
    --navy: #0e4c92;
    --paper: #ffffff;
    --nutrition-band: #fdb733;
    --nutrition-deep: #ff7a00;
    --nutrition-light: #ffb800;
    --nutrition-note: #8a2418;
    --measure-band: #35b5ff;
    --measure-deep: #0050f0;
    --measure-light: #00a8ff;
    --measure-note: #1d2d5c;
    --discipline-band: #ef7789;
    --discipline-deep: #f0284f;
    --discipline-light: #ff6f8a;
    --discipline-note: #a3182b;
    --clarity-band: #34ae9f;
    --clarity-deep: #0a4f48;
    --clarity-light: #10a08f;
    --clarity-note: #10384a;
    --exercise-band: #34d46e;
    --exercise-deep: #05b030;
    --exercise-light: #3ee070;
    --exercise-note: #0b4a22;
  }
  html, body {
    margin: 0;
    padding: 0;
    width: 1200px;
    height: 1200px;
    overflow: hidden;
    background: var(--paper);
  }
  .canvas {
    position: relative;
    width: 1200px;
    height: 1200px;
    background: var(--paper);
  }
  .brand-name {
    position: absolute;
    left: 0;
    width: 1200px;
    top: 316px;
    margin: 0;
    text-align: center;
    font-family: "Poppins", sans-serif;
    font-weight: 500;
    font-size: 50px;
    line-height: 1;
    letter-spacing: 0.32em;
    padding-left: 0.32em;
    box-sizing: border-box;
    color: var(--navy);
  }
  .steps {
    position: absolute;
    left: 0;
    top: 0;
  }
  .step-title {
    font-family: "Oswald", sans-serif;
    font-weight: 400;
    font-size: 64px;
    fill: var(--paper);
  }
  .step-action {
    font-family: "Oswald", sans-serif;
    font-weight: 500;
    font-size: 42px;
  }
  .icon { fill: none; stroke-width: 3.5; stroke-linecap: round; stroke-linejoin: round; }
</style>
</head>
<body>
<main class="canvas">
  <h1 class="brand-name">INNER UPRISING</h1>

  <svg class="steps" width="1200" height="1200" viewBox="0 0 1200 1200" aria-label="Five steps in order: Clarity, Measurement, Discipline, Nutrition, Exercise">
    <defs>
      <radialGradient id="grad-nutrition" cx="45%" cy="70%" r="70%">
        <stop offset="0" stop-color="var(--nutrition-light)"/>
        <stop offset="1" stop-color="var(--nutrition-deep)"/>
      </radialGradient>
      <radialGradient id="grad-measure" cx="40%" cy="70%" r="70%">
        <stop offset="0" stop-color="var(--measure-light)"/>
        <stop offset="1" stop-color="var(--measure-deep)"/>
      </radialGradient>
      <radialGradient id="grad-discipline" cx="45%" cy="65%" r="70%">
        <stop offset="0" stop-color="var(--discipline-light)"/>
        <stop offset="1" stop-color="var(--discipline-deep)"/>
      </radialGradient>
      <radialGradient id="grad-clarity" cx="40%" cy="70%" r="70%">
        <stop offset="0" stop-color="var(--clarity-light)"/>
        <stop offset="1" stop-color="var(--clarity-deep)"/>
      </radialGradient>
      <radialGradient id="grad-exercise" cx="45%" cy="40%" r="70%">
        <stop offset="0" stop-color="var(--exercise-light)"/>
        <stop offset="1" stop-color="var(--exercise-deep)"/>
      </radialGradient>
    </defs>

    <polygon class="band band-clarity" points="651,491 1115,491 1011,588 651,588" fill="var(--clarity-band)"/>
    <polygon class="band band-measure" points="177,618 543,618 543,715 73,715" fill="var(--measure-band)"/>
    <polygon class="band band-discipline" points="651,746 1115,746 1011,842 651,842" fill="var(--discipline-band)"/>
    <polygon class="band band-nutrition" points="177,870 543,870 543,966 73,966" fill="var(--nutrition-band)"/>
    <polygon class="band band-exercise" points="651,999 1128,999 1024,1096 651,1096" fill="var(--exercise-band)"/>

    <g class="step step-clarity">
      <circle cx="599" cy="540" r="73" fill="var(--paper)"/>
      <circle cx="599" cy="540" r="67" fill="url(#grad-clarity)"/>
      <circle cx="599" cy="540" r="42" fill="var(--paper)"/>
      <g class="icon" stroke="var(--clarity-light)">
        <path d="M599,564 L592,556 C578,553 570,543 572,530 C575,517 587,510 599,510 C611,510 623,517 626,530 C628,543 620,553 606,556 Z"/>
        <path d="M583,534 C592,524 606,524 615,534 C606,541 592,541 583,534 Z" stroke-width="2.5"/>
        <circle cx="599" cy="533" r="3" fill="var(--clarity-light)" stroke="none"/>
      </g>
      <text class="step-title" x="699" y="563" textLength="138" lengthAdjust="spacingAndGlyphs">CLARITY</text>
      <text class="step-action" x="855" y="558" textLength="84" lengthAdjust="spacingAndGlyphs" fill="var(--clarity-note)">(SEE IT)</text>
    </g>

    <g class="step step-measure">
      <circle cx="599" cy="666" r="73" fill="var(--paper)"/>
      <circle cx="599" cy="666" r="67" fill="url(#grad-measure)"/>
      <circle cx="599" cy="666" r="42" fill="var(--paper)"/>
      <g class="icon" stroke="var(--measure-light)" stroke-width="2.5">
        <rect x="571" y="663" width="56" height="18"/>
        <path d="M571,648 L627,648 M571,643 L571,653 M627,643 L627,653 M578,663 V669 M585,663 V673 M592,663 V669 M599,663 V673 M606,663 V669 M613,663 V673 M620,663 V669"/>
      </g>
      <text class="step-title" x="169" y="689" textLength="226" lengthAdjust="spacingAndGlyphs">MEASUREMENT</text>
      <text class="step-action" x="405" y="684" textLength="116" lengthAdjust="spacingAndGlyphs" fill="var(--measure-note)">(TRACK IT)</text>
    </g>

    <g class="step step-discipline">
      <circle cx="599" cy="789" r="73" fill="var(--paper)"/>
      <circle cx="599" cy="789" r="67" fill="url(#grad-discipline)"/>
      <circle cx="599" cy="789" r="42" fill="var(--paper)"/>
      <g class="icon" stroke="var(--discipline-deep)">
        <rect x="580" y="770" width="38" height="44" rx="3"/>
        <rect x="591" y="765" width="16" height="8" rx="2"/>
        <path d="M587,784 H611 M587,794 H611 M587,804 H611"/>
      </g>
      <text class="step-title" x="694" y="817" textLength="178" lengthAdjust="spacingAndGlyphs">DISCIPLINE</text>
      <text class="step-action" x="890" y="812" textLength="74" lengthAdjust="spacingAndGlyphs" fill="var(--discipline-note)">(DO IT)</text>
    </g>

    <g class="step step-nutrition">
      <circle cx="599" cy="917" r="73" fill="var(--paper)"/>
      <circle cx="599" cy="917" r="67" fill="url(#grad-nutrition)"/>
      <circle cx="599" cy="917" r="42" fill="var(--paper)"/>
      <path class="icon" stroke="var(--nutrition-light)" d="M599,943 L578,922 C568,912 570,897 582,894 C590,892 596,896 599,902 C602,896 608,892 616,894 C628,897 630,912 620,922 Z"/>
      <circle class="icon" stroke="var(--nutrition-light)" cx="603" cy="929" r="6"/>
      <text class="step-title" x="245" y="940" textLength="174" lengthAdjust="spacingAndGlyphs">NUTRITION</text>
      <text class="step-action" x="435" y="935" textLength="83" lengthAdjust="spacingAndGlyphs" fill="var(--nutrition-note)">(EAT IT)</text>
    </g>

    <g class="step step-exercise">
      <circle cx="599" cy="1048" r="73" fill="var(--paper)"/>
      <circle cx="599" cy="1048" r="67" fill="url(#grad-exercise)"/>
      <circle cx="599" cy="1048" r="42" fill="var(--paper)"/>
      <g class="icon" stroke="var(--exercise-deep)" stroke-width="4">
        <path d="M581,1048 H617"/>
        <rect x="575" y="1036" width="6" height="24" rx="2" fill="var(--exercise-deep)"/>
        <rect x="617" y="1036" width="6" height="24" rx="2" fill="var(--exercise-deep)"/>
        <path d="M569,1041 V1055 M629,1041 V1055"/>
      </g>
      <text class="step-title" x="706" y="1071" textLength="154" lengthAdjust="spacingAndGlyphs">EXERCISE</text>
      <text class="step-action" x="874" y="1066" textLength="105" lengthAdjust="spacingAndGlyphs" fill="var(--exercise-note)">(MOVE IT)</text>
    </g>
  </svg>
</main>
</body>
</html>
```